依頼詳細
送付先は、行政関係者、企業の経営者などの専門家を想定しております。
当社のロゴを引き立たせて頂き、高級感があり洗練されたデザインを希望します。
封筒の色は、グレー系を予定しておりますので、フォントの色など調整お願いいたします。
記載項目
住所、会社名、会社ロゴ、電話番号、FAX番号、WEBアドレス
希望イメージ
シンプル 複雑
単色 カラフル
暗い 明るい
日常 高級
遊び心 厳粛
未来的 伝統的
女性的 男性的
希望する色
納品ファイル
• イラストレーター形式 (.ai)
補足説明
希望のデザインの色ですが、青色系でお願いいたします。

添付フャイルが上がっておりませんでしたので、添付いたします。

またデザインは、イラストレータ(ai形式)とjpg形式の2種類
の製作をお願いたします。

よろしくおねがいいたします。

の製作をお願いたします。

よろしくおねがいいたします。

シンプルかつ上品なデザインでしたので、こちらを選ばせて頂きました。

たくさんの提案を頂き、ありがとうございます。
今後ともご縁がありましたら、宜しく御願い申し上げます。

```html
<!DOCTYPE html>
<html lang="ja">
<head>
<meta charset="utf-8">
<title>NV Advisory Envelope</title>
<link rel="stylesheet" href="https://fonts.googleapis.com/css2?family=Crimson+Pro:wght@600&family=Noto+Sans+JP:wght@400;500;700&display=swap">
<style>
  :root {
    --paper: #ffffff;
    --envelope: #dcdcdc;
    --envelope-edge: #6f6f6f;
    --navy: #1d2f6b;
    --ink: #2a2a2a;
    --accent-red: #d7262e;
  }
  html, body {
    margin: 0;
    padding: 0;
    width: 1200px;
    height: 2620px;
    overflow: hidden;
    background: var(--paper);
  }
  .envelope {
    position: relative;
    width: 1200px;
    height: 2620px;
  }
  .envelope-shape {
    position: absolute;
    inset: 0;
  }
  .brand {
    position: absolute;
    left: 160px;
    top: 2078px;
    display: flex;
    align-items: center;
    gap: 30px;
  }
  .brand-square {
    width: 70px;
    height: 70px;
    background: var(--navy);
  }
  .brand-name {
    font-family: "Crimson Pro", serif;
    font-weight: 600;
    font-size: 86px;
    line-height: 1;
    color: var(--navy);
    letter-spacing: 1px;
  }
  .sender {
    position: absolute;
    left: 176px;
    top: 2198px;
    padding-left: 38px;
    border-left: 8px solid var(--accent-red);
    font-family: "Noto Sans JP", sans-serif;
  }
  .sender-company {
    font-size: 42px;
    font-weight: 500;
    color: var(--ink);
    line-height: 1.3;
    margin: 0 0 10px;
  }
  .sender-address {
    font-size: 29px;
    color: var(--ink);
    line-height: 1.3;
    margin: 0 0 10px;
  }
  .sender-phone,
  .sender-web {
    font-size: 38px;
    font-weight: 700;
    color: var(--navy);
    line-height: 1.3;
    margin: 0 0 8px;
    letter-spacing: 0.5px;
  }
  .sender-phone span + span { margin-left: 34px; }
</style>
</head>
<body>
  <main class="envelope">
    <svg class="envelope-shape" width="1200" height="2620" viewBox="0 0 1200 2620" aria-hidden="true">
      <polygon points="72,4 1128,4 1196,140 1196,2616 4,2616 4,140" fill="var(--envelope)" stroke="var(--envelope-edge)" stroke-width="4"/>
      <line x1="4" y1="140" x2="1196" y2="140" stroke="var(--envelope-edge)" stroke-width="3"/>
    </svg>

    <div class="brand">
      <div class="brand-square"></div>
      <div class="brand-name">NV Advisory Inc.</div>
    </div>

    <section class="sender">
      <p class="sender-company">株式会社NVアドバイザリー</p>
      <p class="sender-address">〒100-0005&nbsp; 東京都千代田区丸の内9-9-9 サンプルビル7階</p>
      <p class="sender-phone"><span>TEL 03-5550-0142</span><span>FAX 03-5550-0143</span></p>
      <p class="sender-web">http://www.nv-advisory.co.jp</p>
    </section>
  </main>
</body>
</html>
```